Der erste 100% elektrische Schulbus braucht ein wunderschönes Hingucker-Design
Ein tolles Design mit hoher Qualität und Präzision für unseren Schulbus. Jorik ist sehr nett, hilfsbereit und proaktiv. Unser Briefing hat er kreativ zu unserer vollsten Zufriedenheit umgesetzt.
Zielgruppe
Wir glauben daran, auf kindgerechte Weise neue Fähigkeiten zu lehren und zu lernen. Wir bieten unseren Kindern einen Raum der Entdeckung und Offenheit. Unsere private Schule wird von Eltern geführt und ist von einem starken Gemeinschaftsgefühl geprägt. Sie bietet Kindern im Alter von 3 bis 12 Jahren Montessori-Bildung von höchster Qualität in Le Vallon in der französischsprachigen Schweiz (Nähe Genf).
Wir bieten einen zweisprachiges Ansatz (Englisch und Französisch) für die Kleinsten, einen dreisprachigen Ansatz (Englisch, Französisch und Deutsch) für die Älteren, frisch zubereitete Mahlzeiten und eine ganztägige Betreuung.
Unsere Schule bietet eine tägliche Schulbusverbindung von Nyon und den umliegenden Gemeinden zum Campus Le Vallon an. Wir beschäftigen unseren eigenen Fahrer und betreiben unseren eigenen Schulbus. Der Service ist für Eltern kostenlos und von den kantonalen Behörden genehmigt.
Wir glauben fest an Nachhaltigkeit und wollen ein Beispiel geben und zeigen, dass emissionsfreie Schülertransporte möglich und wirtschaftlich sind.
Aufgabenstellung
Bitte schaut Euch das Briefing im hochgeladenen PDF an.

```html
<!DOCTYPE html>
<html lang="en">
<head>
<meta charset="utf-8">
<title>Trois Cent Pétales – Electric Schoolbus Wrap</title>
<link rel="stylesheet" href="https://fonts.googleapis.com/css2?family=Nunito:wght@400;800;900&display=swap">
<style>
  :root {
    --bg: #ffffff;
    --panel-grey: #58595b;
    --lime: #c4cc0b;
    --leaf-green: #9bb81f;
    --olive: #5b6f27;
    --text-dark: #5b6f27;
    --white: #ffffff;
    --photo-warm: #d9894a;
    --photo-light: #ece3da;
  }
  html, body {
    margin: 0;
    width: 1200px;
    height: 848px;
    overflow: hidden;
    background: var(--bg);
  }
  .wrap-layout {
    display: block;
    width: 1200px;
    height: 848px;
    font-family: "Nunito", sans-serif;
  }
  .window-panel { fill: var(--panel-grey); }
  .leaf-lime { fill: var(--lime); }
  .leaf-green { fill: var(--leaf-green); }
  .leaf-olive { fill: var(--olive); }
  .txt-heavy { font-weight: 900; }
  .txt-bold { font-weight: 800; }
  .txt-regular { font-weight: 400; }
  .fill-white { fill: var(--white); }
  .fill-dark { fill: var(--text-dark); }
  .fill-lime { fill: var(--lime); }
  .brand-mark { fill: var(--lime); }
</style>
</head>
<body>
<svg class="wrap-layout" viewBox="0 0 1200 848" xmlns="http://www.w3.org/2000/svg">
  <defs>
    <linearGradient id="photoTone" x1="0" y1="0" x2="1" y2="1">
      <stop offset="0" stop-color="#8a6a55"/>
      <stop offset="0.45" stop-color="var(--photo-warm)"/>
      <stop offset="1" stop-color="var(--photo-light)"/>
    </linearGradient>
  </defs>

  <!-- window band -->
  <rect class="window-panel" x="500" y="270" width="589" height="140" rx="14"/>

  <!-- photo area -->
  <g role="img" aria-label="Photo of a laughing red-haired girl with a butterfly on her nose">
    <path d="M742 286 H1000 Q1020 380 1018 540 H742 Q726 420 742 286 Z" fill="url(#photoTone)" opacity="0.9"/>
  </g>

  <!-- website leaf -->
  <path class="leaf-green" d="M457 196 Q560 190 646 191 Q660 205 667 218 Q610 252 552 252 Q495 250 457 196 Z"/>
  <text class="txt-heavy fill-white" x="570" y="214" font-size="14" text-anchor="middle">www.</text>
  <text class="txt-heavy fill-dark" x="570" y="228" font-size="14" text-anchor="middle">troiscentpetales.ch</text>

  <!-- multilingual leaf -->
  <path class="leaf-lime" d="M910 195 Q1020 196 1106 201 Q1060 252 996 257 Q940 255 897 224 Z"/>
  <text class="txt-heavy fill-white" x="988" y="225" font-size="24" transform="rotate(-5 988 225)" text-anchor="middle">multi</text>
  <text class="txt-heavy fill-dark" x="1006" y="240" font-size="15" transform="rotate(-7 1006 240)" text-anchor="middle">lingual</text>

  <!-- school name -->
  <circle class="brand-mark" cx="545" cy="340" r="12"/>
  <text class="txt-bold fill-white" x="577" y="354" font-size="15">Ecole Montessori</text>
  <text class="txt-bold fill-white" x="577" y="373" font-size="15">Trois Cent Pétales</text>

  <!-- electric leaf -->
  <path class="leaf-olive" d="M223 522 Q262 476 330 474 Q370 476 400 487 Q385 530 366 551 L258 552 Q236 540 223 522 Z"/>
  <text class="txt-heavy fill-lime" x="265" y="501" font-size="38">100%</text>
  <text class="txt-bold fill-white" x="262" y="520" font-size="15">electric</text>
  <text class="txt-bold fill-white" x="276" y="537" font-size="15">schoolbus</text>

  <!-- age leaf -->
  <path class="leaf-lime" d="M536 434 Q600 428 650 446 Q720 480 743 543 L566 543 Q540 490 536 434 Z"/>
  <text class="txt-regular fill-dark" x="570" y="477" font-size="19">For kids</text>
  <text class="txt-heavy fill-dark" x="580" y="518" font-size="38">3</text>
  <text class="txt-heavy fill-white" x="611" y="494" font-size="14">from</text>
  <text class="txt-heavy fill-white" x="615" y="512" font-size="14">to</text>
  <text class="txt-heavy fill-dark" x="638" y="518" font-size="27">12</text>

  <!-- location leaf -->
  <path class="leaf-green" d="M990 432 Q1050 416 1108 442 L1108 512 Q1060 532 1012 534 Q995 480 990 432 Z"/>
  <text class="txt-heavy fill-white" x="1014" y="475" font-size="15">Le Vallon</text>
</svg>
</body>
</html>
```